Lotus Leaf Kitchen Road Billboard

Road Billboard I need all of this information on it
Authentic Thai Food Bangkok Style
6.5 Miles on the right
4126 Maple Ridge Rd Otto NC
828-555-4172

```html
<!DOCTYPE html>
<html lang="en">
<head>
<meta charset="utf-8">
<title>Lotus Leaf Kitchen – Road Billboard</title>
<link href="https://fonts.googleapis.com/css2?family=Cinzel:wght@700&family=Oswald:wght@500;600&display=swap" rel="stylesheet">
<style>
  :root {
    --ink: #000000;
    --paper: #ffffff;
    --gold: #d9ae2c;
    --red: #e31d2b;
    --flame-deep: #1a0d06;
    --flame-mid: #7a2a08;
    --flame-hot: #e8731c;
    --address-band: rgba(20, 10, 6, 0.78);
    --stage: #f2f2f2;
  }
  html, body {
    margin: 0;
    padding: 0;
    width: 1037px;
    height: 1200px;
    overflow: hidden;
    background: var(--stage);
  }
  .canvas {
    width: 1037px;
    height: 1200px;
    display: flex;
    align-items: center;
    justify-content: center;
  }
  .billboard {
    display: block;
    width: 1037px;
    height: 517px;
  }
  .headline-serif {
    font-family: "Cinzel", "Times New Roman", serif;
    font-weight: 700;
  }
  .condensed {
    font-family: "Oswald", "Arial Narrow", sans-serif;
    font-weight: 600;
  }
  .brand-name {
    font-family: "Oswald", "Arial Narrow", sans-serif;
    font-weight: 500;
    fill: var(--gold);
  }
</style>
</head>
<body>
<main class="canvas">
  <svg class="billboard" viewBox="0 0 1123 560" xmlns="http://www.w3.org/2000/svg">
    <defs>
      <radialGradient id="flameGlow" cx="0.55" cy="0.55" r="0.75">
        <stop offset="0" stop-color="var(--flame-hot)"/>
        <stop offset="0.45" stop-color="var(--flame-mid)"/>
        <stop offset="1" stop-color="var(--flame-deep)"/>
      </radialGradient>
    </defs>

    <!-- Food photograph area -->
    <rect class="food-photo" x="520" y="0" width="603" height="560" fill="url(#flameGlow)"
          role="img" aria-label="Photo of shrimp, broccoli and vegetables tossed in a flaming wok"/>

    <!-- Headline panel -->
    <polygon class="headline-panel" points="0,0 540,0 580,298 0,298" fill="var(--ink)"/>
    <text class="headline-serif" x="52" y="84" font-size="50" fill="var(--gold)">AUTHENTIC</text>
    <text class="headline-serif" x="52" y="148" font-size="50" fill="var(--paper)">THAI FOOD</text>
    <text class="headline-serif" x="52" y="212" font-size="50" fill="var(--red)">BANGKOK</text>
    <text class="headline-serif" x="52" y="275" font-size="50" fill="var(--red)">STYLEA</text>

    <!-- Brand seal -->
    <g class="brand-seal">
      <circle cx="467" cy="158" r="111" fill="var(--ink)" stroke="var(--red)" stroke-width="6"/>
      <text class="brand-name" x="467" y="150" font-size="30" text-anchor="middle">Lotus Leaf</text>
      <text class="brand-name" x="467" y="188" font-size="30" text-anchor="middle">Kitchen</text>
    </g>

    <!-- Direction arrow -->
    <polygon class="direction-arrow" points="0,306 585,306 595,290 665,362 595,434 585,418 0,418"
             fill="var(--red)" stroke="var(--paper)" stroke-width="5"/>
    <text class="condensed" x="32" y="388" font-size="64" fill="var(--paper)">6.5 Miles on the right</text>

    <!-- Phone panel -->
    <polygon class="phone-panel" points="0,426 603,426 622,560 0,560" fill="var(--ink)"/>
    <text class="condensed" x="44" y="513" font-size="88" fill="var(--paper)">828-555-4172</text>

    <!-- Address band -->
    <polygon class="address-band" points="614,448 1123,448 1123,514 622,514" fill="var(--address-band)"/>
    <text class="condensed" x="630" y="497" font-size="40" fill="var(--paper)">4126 Maple Ridge Rd Otto NC</text>
  </svg>
</main>
</body>
</html>
```